Garden Maintenance business card

I need a business card design for my new business "Silver Birch Garden Co". I do garden maintenance including lawns, turf lawn, pruning, hedging, water systems, anything related to the garden really (dont think i need to include any of that except garden maintenance)

Reason: narrowed it down and just showing my business partners the designs, cheers

Industry/Entity Type

Business

Requirements
Must have
• Must Have:
- ABN: XX XXX XXX XXX
Mobile phone number 00 0000000
email address xxxx.xxxxxx@gmail.com
Owner Name Xxxx xxxxxx
title: garden specialist possibly under name or something sounding professional
logo which has been submitted both with a background and one without, feel free to choose whichever one you like
business name

```html
<!DOCTYPE html>
<html lang="en">
<head>
<meta charset="utf-8">
<title>Silver Birch Garden Co — Business Card</title>
<link rel="stylesheet" href="https://fonts.googleapis.com/css2?family=Cabin:wght@400&family=Crimson+Text:ital@0;1&display=swap">
<style>
  :root {
    --paper: #f5f4ef;
    --ink: #1e1e1e;
    --band: #8fbe74;
    --band-light: #a8cf90;
    --panel: #b9d8a4;
    --band-text: #1f2a14;
    --hand-skin: #ebe3d6;
    --hand-green: #9cc783;
  }
  * { margin: 0; padding: 0; box-sizing: border-box; }
  html, body { width: 735px; height: 1200px; overflow: hidden; background: var(--paper); }
  .card {
    position: relative;
    width: 735px;
    height: 1200px;
    background: var(--paper);
    font-family: "Cabin", "Gill Sans", sans-serif;
    color: var(--ink);
    overflow: hidden;
  }
  .business-name {
    position: absolute;
    left: 0; top: 0;
    width: 735px; height: 260px;
  }
  .business-name text {
    font-family: "Crimson Text", Georgia, serif;
    font-size: 60px;
    fill: var(--ink);
  }
  .illustration {
    position: absolute;
    left: 400px; top: 150px;
    width: 320px; height: 600px;
    border-radius: 140px 140px 60px 60px;
    background: radial-gradient(ellipse at 45% 25%, var(--hand-green) 0%, rgba(156,199,131,0.5) 28%, var(--hand-skin) 55%, rgba(235,227,214,0) 80%);
  }
  .owner-name {
    position: absolute;
    left: 40px; top: 425px;
    font-size: 58px;
    font-weight: 400;
  }
  .owner-title {
    position: absolute;
    left: 103px; top: 502px;
    font-family: "Crimson Text", Georgia, serif;
    font-style: italic;
    font-size: 42px;
  }
  .contact {
    position: absolute;
    left: 40px;
    font-size: 27px;
    line-height: 1;
  }
  .contact-abn { top: 654px; }
  .contact-mobile { top: 691px; }
  .contact-email { top: 762px; }

  .service-band {
    position: absolute;
    left: 0; top: 826px;
    width: 735px; height: 374px;
    background: var(--band);
  }
  .service-band-lower {
    position: absolute;
    left: 311px; top: 122px;
    width: 424px; height: 252px;
    background: var(--band-light);
  }
  .mark-panel {
    position: absolute;
    left: 0; top: 0;
    width: 311px; height: 326px;
    background: var(--panel);
  }
  .mark-panel-emblem {
    position: absolute;
    left: 58px; top: 120px;
    width: 190px; height: 190px;
    border-radius: 50%;
    background: radial-gradient(circle, rgba(143,190,116,0.55) 0%, rgba(143,190,116,0) 70%);
  }
  .service-heading {
    position: absolute;
    left: 355px; top: 50px;
    font-family: "Crimson Text", Georgia, serif;
    font-style: italic;
    font-size: 44px;
    color: var(--band-text);
  }
  .service-list {
    position: absolute;
    left: 311px; top: 135px;
    width: 424px;
    text-align: center;
    font-size: 31px;
    line-height: 40px;
    color: var(--band-text);
  }
  .website {
    position: absolute;
    left: 311px; top: 296px;
    width: 424px;
    text-align: center;
    font-size: 30px;
    color: var(--band-text);
  }
</style>
</head>
<body>
<main class="card">
  <svg class="business-name" viewBox="0 0 735 260" aria-label="Silver Birch Garden Co">
    <defs>
      <path id="name-arc" d="M 30 215 Q 330 40 710 130"/>
    </defs>
    <text><textPath href="#name-arc">Silver Birch Garden Co</textPath></text>
  </svg>

  <div class="illustration" role="img" aria-label="Drawing of a thumbs-up hand with a green sapling growing from the thumb"></div>

  <h1 class="owner-name">Tom Hartley</h1>
  <p class="owner-title">Garden Guru</p>

  <p class="contact contact-abn">ABN: XX XXX XXX XXX</p>
  <p class="contact contact-mobile">Mobile: 00 0000000</p>
  <p class="contact contact-email">xxxx.xxxxxx@gmail.com</p>

  <section class="service-band">
    <div class="service-band-lower"></div>
    <div class="mark-panel">
      <div class="mark-panel-emblem" role="img" aria-label="Faint sapling emblem"></div>
    </div>
    <h2 class="service-heading">Garden Maintenance</h2>
    <p class="service-list">lawns • turf lawn • pruning<br>water systems • hedging</p>
    <p class="website">www.websiteaddress.com</p>
  </section>
</main>
</body>
</html>
```